Backdrop design that will flow throughout my Website

Name of my company is Maple Fern’s Mentoring

I would like you to provide designs of the Bee and drops of Honey...this will be

Target Market(s)

My targeted audiences are females, ages 40-55

Font styles to use
Script

Colors
6b449b
f37122
fbca95
e4daeb

Requirements
Must have
• Color concepts (orange, purple, and gray) with variations of brown for the Bee …see logo
Nice to have
• See sample FILE #6 below!! See the recessed flower in the background??

```html
<!DOCTYPE html>
<html lang="en">
<head>
<meta charset="utf-8">
<title>Maple Fern’s Mentoring — Backdrop</title>
<link href="https://fonts.googleapis.com/css2?family=Libre+Baskerville:wght@400;700&family=Great+Vibes&display=swap" rel="stylesheet">
<style>
  :root {
    --purple: #872a88;
    --purple-soft: #b784b8;
    --ink: #221c1a;
    --white: #ffffff;
    --page: #eeeeee;
    --honey-light: #f6c36a;
    --honey-mid: #e08a1c;
    --honey-deep: #9a4a0c;
  }
  * { margin: 0; padding: 0; box-sizing: border-box; }
  html, body {
    width: 1183px; height: 1200px; overflow: hidden;
    background: var(--page);
  }
  .backdrop {
    position: absolute; left: 41px; top: 50px;
    width: 935px; height: 934px;
    transform: scale(1.1765); transform-origin: 0 0;
    background: var(--white); overflow: hidden;
    font-family: "Libre Baskerville", Georgia, serif;
  }
  .honey-photo {
    position: absolute; left: 525px; top: 0; width: 410px; height: 600px;
    background: radial-gradient(ellipse at 60% 70%, var(--honey-light) 0%, var(--honey-mid) 45%, var(--honey-deep) 100%);
    border-bottom-left-radius: 140px;
  }
  .brand {
    position: absolute; left: 270px; top: 120px; width: 390px;
    display: flex; align-items: center; gap: 14px;
    color: var(--purple); font-weight: 700; font-size: 29px; line-height: 1.2;
  }
  .brand-dot {
    flex: none; width: 26px; height: 26px; border-radius: 50%;
    background: var(--purple);
  }
  .presenter {
    position: absolute; left: 37px; top: 358px; width: 500px; text-align: center;
  }
  .presenter-name {
    font-weight: 700; font-size: 33px; color: var(--ink); letter-spacing: 0.5px;
  }
  .presenter-role {
    margin-top: 4px; font-size: 27px; color: var(--purple);
  }
  .presenter-rule {
    display: block; margin: 2px 0 0 230px; width: 46px; height: 2px; background: var(--purple);
  }
  .band { position: absolute; left: 0; top: 0; width: 935px; height: 934px; }
  .bee-art {
    position: absolute; left: 118px; top: 508px; width: 92px; height: 106px;
    background: radial-gradient(circle at 55% 55%, #f4d23a 0%, #3a2a1a 60%, #7a3f8a 100%);
    border-radius: 46%;
  }
  .quote {
    position: absolute; left: 0; top: 550px; width: 935px; text-align: center; color: var(--white);
  }
  .quote-mark {
    display: flex; align-items: center; justify-content: center; gap: 12px;
    color: var(--purple-soft); font-size: 34px; font-weight: 700; height: 30px;
  }
  .quote-mark::before, .quote-mark::after {
    content: ""; width: 195px; height: 2px; background: var(--white);
  }
  .quote-line1 { margin-top: 14px; font-weight: 700; font-size: 44px; line-height: 1.15; }
  .quote-line2 {
    display: inline-block; margin-top: 4px; padding: 1px 16px;
    background: var(--white); color: var(--purple); font-weight: 700; font-size: 44px; line-height: 1.05;
  }
  .quote-script { font-family: "Great Vibes", cursive; font-size: 96px; line-height: 0.95; }
  .quote-mark.closing { margin-top: 22px; }
  .attribution { margin-top: 26px; font-size: 27px; letter-spacing: 2px; }
</style>
</head>
<body>
  <main class="backdrop">
    <div class="honey-photo" role="img" aria-label="Photo of a honey dipper dripping honey into a glass jar"></div>

    <div class="brand"><span class="brand-dot"></span><span>Maple Fern’s Mentoring</span></div>

    <div class="presenter">
      <p class="presenter-name">CARLA WHITMORE, MBA</p>
      <p class="presenter-role">Serial Entrepreneur</p>
      <span class="presenter-rule"></span>
    </div>

    <svg class="band" viewBox="0 0 935 934" aria-hidden="true">
      <path d="M0 562 Q 470 488 935 552 L935 934 L0 934 Z" fill="var(--purple)"/>
      <path d="M150 534 Q 520 486 935 566" fill="none" stroke="var(--purple)" stroke-width="3"/>
    </svg>

    <div class="bee-art" role="img" aria-label="Illustration of a cartoon bee"></div>

    <blockquote class="quote">
      <div class="quote-mark">“</div>
      <p class="quote-line1">BEES MAKE HONEY,</p>
      <p class="quote-line2">ENTREPRENEURS MAKE</p>
      <p class="quote-script">Money</p>
      <div class="quote-mark closing">”</div>
      <p class="attribution">-Business Strategist</p>
    </blockquote>
  </main>
</body>
</html>
```